Robotic consulting firm needs a Powerpoint Template

I'm looking for a powerpoint template for my consulting business. We are in the robotic field and needs to present project concept or robotic cell layout to the client. I'm looking for a design that is professionnal and using my logo. Our color is purple, but I don't want to overuse the color everywhere, it needs to look professionnal for the engineer field. Color code is 9F35D8

```html
<!DOCTYPE html>
<html lang="en">
<head>
<meta charset="utf-8">
<title>Kinetra Presentation Template</title>
<link rel="stylesheet" href="https://fonts.googleapis.com/css2?family=Montserrat:ital,wght@0,400;0,500;0,600;0,700;1,500&display=swap">
<style>
  :root{
    --purple:#9F35D8;
    --ink:#222222;
    --dark:#2a2a2c;
    --muted:#6d6d70;
    --rule:#cfcfd3;
    --stage:#e4e4e7;
    --paper:#ffffff;
  }
  html,body{margin:0;padding:0;width:906px;height:1200px;overflow:hidden;background:var(--stage);}
  .deck{
    display:grid;grid-template-columns:repeat(3,266px);grid-auto-rows:150px;
    column-gap:15px;row-gap:13px;padding:36px 0 0 39px;
  }
  .slide{width:266px;height:150px;display:block;background:var(--paper);box-shadow:0 1px 3px rgba(0,0,0,.18);
    font-family:"Montserrat",sans-serif;}
  .fill-purple{fill:var(--purple);} .fill-ink{fill:var(--ink);} .fill-dark{fill:var(--dark);} .fill-white{fill:#fff;}
  .stroke-ink{stroke:var(--ink);fill:none;} .stroke-purple{stroke:var(--purple);fill:none;}
  .rule{stroke:var(--rule);stroke-width:.8;}
  .h1{font-weight:700;font-size:30px;fill:var(--ink);}
  .h2{font-weight:700;font-size:15px;fill:var(--ink);}
  .h3{font-weight:700;font-size:7px;fill:var(--ink);}
  .h3p{font-weight:700;font-size:7px;fill:var(--purple);}
  .fine{font-size:4.2px;fill:var(--muted);}
  .fine-w{font-size:4.2px;fill:#d8d8d8;}
  .small{font-size:6px;fill:var(--muted);}
  .brand-sm{font-weight:700;font-size:5.5px;fill:var(--purple);letter-spacing:.5px;}
  .pg{font-size:5px;fill:var(--ink);}
  .w{fill:#fff;} .p{fill:var(--purple);}
  .label{font-weight:700;font-size:6px;fill:var(--purple);}
</style>
</head>
<body>
<svg width="0" height="0" style="position:absolute" aria-hidden="true">
  <defs>
    <linearGradient id="photo-dark" x1="0" y1="0" x2="1" y2="1"><stop offset="0" stop-color="#3a3a3d"/><stop offset="1" stop-color="#1c1c1e"/></linearGradient>
    <linearGradient id="photo-grey" x1="0" y1="0" x2="1" y2="1"><stop offset="0" stop-color="#b9b9bd"/><stop offset="1" stop-color="#5c5c60"/></linearGradient>
    <linearGradient id="photo-light" x1="0" y1="0" x2="0" y2="1"><stop offset="0" stop-color="#d6d6d9"/><stop offset="1" stop-color="#8a8a8e"/></linearGradient>
  </defs>
</svg>

<main class="deck">

<!-- 1 Cover -->
<svg class="slide" viewBox="0 0 491 276">
  <rect width="491" height="276" fill="url(#photo-dark)" role="img" aria-label="Dark industrial robotics photo"/>
  <rect x="150" y="126" width="18" height="18" class="fill-purple"/>
  <text x="205" y="148" font-size="34" font-weight="600" letter-spacing="7" class="w">KINETRA</text>
  <rect x="196" y="161" width="295" height="22" class="fill-purple"/>
  <text x="202" y="176" font-size="11" font-weight="500" letter-spacing="1" class="w">Presentation Business Marketing</text>
  <text x="266" y="197" font-size="7" letter-spacing="2.5" class="w">www.kinetra.io</text>
</svg>

<!-- 2 Title -->
<svg class="slide" viewBox="0 0 491 276">
  <rect x="10" y="10" width="11" height="11" class="fill-ink"/>
  <rect x="48" y="58" width="12" height="12" class="fill-purple"/>
  <text x="30" y="106" font-size="11" font-weight="700" letter-spacing="2.5" class="p">KINETRA</text>
  <text x="30" y="150" font-size="26" font-weight="700" class="fill-ink">Business</text>
  <text x="30" y="174" font-size="18" font-weight="600" class="fill-ink">Marketing</text>
  <text x="30" y="208" font-size="10" font-style="italic" font-weight="500" class="p">Presentation</text>
  <text x="30" y="220" class="fine" font-style="italic">Lorem ipsum dolor sit amet, consectetuer</text>
  <text x="30" y="227" class="fine" font-style="italic">adipiscing elit, sed diam nonum</text>
  <circle cx="33" cy="252" r="2.3" class="fill-ink"/><circle cx="42" cy="252" r="2.3" class="fill-purple"/><circle cx="51" cy="252" r="2.3" class="fill-ink"/>
  <rect x="206" y="0" width="285" height="224" fill="url(#photo-grey)" role="img" aria-label="Engineer with laptop and digital network icons"/>
  <rect x="206" y="224" width="285" height="52" class="fill-purple"/>
  <text x="286" y="254" font-size="7" letter-spacing="3" class="w">www.kinetra-studio.com</text>
</svg>

<!-- 3 Agenda -->
<svg class="slide" viewBox="0 0 491 276">
  <rect x="70" y="114" width="4" height="37" class="fill-purple"/>
  <text x="80" y="143" class="h1">Agenda</text>
  <g>
    <text x="230" y="66" font-size="8" font-weight="600"><tspan class="p">1.</tspan> <tspan class="fill-ink">Lorem ipsum</tspan></text>
    <text x="240" y="76" class="fine">Lorem ipsum dolor sit amet, consectetuer adipiscing elit, sed</text><text x="240" y="82" class="fine">diam nonummy nibh euismod tincid</text>
    <text x="230" y="111" font-size="8" font-weight="600"><tspan class="p">2.</tspan> <tspan class="fill-ink">Lorem ipsum</tspan></text>
    <text x="240" y="121" class="fine">Lorem ipsum dolor sit amet, consectetuer adipiscing elit, sed</text><text x="240" y="127" class="fine">diam nonummy nibh euismod tincid</text>
    <text x="230" y="156" font-size="8" font-weight="600"><tspan class="p">3.</tspan> <tspan class="fill-ink">Lorem ipsum</tspan></text>
    <text x="240" y="166" class="fine">Lorem ipsum dolor sit amet, consectetuer adipiscing elit, sed</text><text x="240" y="172" class="fine">diam nonummy nibh euismod tincid</text>
    <text x="230" y="199" font-size="8" font-weight="600"><tspan class="p">4.</tspan> <tspan class="fill-ink">Lorem ipsum</tspan></text>
    <text x="240" y="209" class="fine">Lorem ipsum dolor sit amet, consectetuer adipiscing elit, sed</text><text x="240" y="215" class="fine">diam nonummy nibh euismod tincid</text>
  </g>
  <rect x="10" y="253" width="7" height="7" class="fill-purple"/><text x="20" y="259" class="brand-sm">KINETRA</text>
  <line x1="50" y1="261" x2="480" y2="261" class="rule"/><text x="478" y="262" class="pg" text-anchor="end">2</text>
</svg>

<!-- 4 Intro -->
<svg class="slide" viewBox="0 0 491 276">
  <text x="24" y="36" font-size="14" font-weight="700" class="fill-ink">Lorem Ipsum</text>
  <text x="24" y="57" font-size="14" font-weight="700" class="fill-ink">Dolor Sit</text>
  <text x="24" y="78" font-size="14" font-weight="700" class="fill-ink">Ametkeeper.</text>
  <rect x="24" y="92" width="14" height="2" class="fill-purple"/><rect x="40" y="92" width="4" height="2" class="fill-ink"/>
  <g class="fine">
    <text x="24" y="108">Lorem ipsum dolor sit amet, consec-</text><text x="24" y="114">tetuer adipiscing elit, sed diam nonum-</text><text x="24" y="120">my nibh euismod tincidunt ut laoreet</text><text x="24" y="126">dolore magna aliquam erat volutpat.</text>
    <text x="24" y="140">Ut wisi enim ad minim veniam, quis</text><text x="24" y="146">nostrud exerci tation ullamcorper</text><text x="24" y="152">suscipit lobortis nisl ut aliquip ex ea</text><text x="24" y="158">commodo consequat. Duis autem vel</text><text x="24" y="164">eum iriure dolor in hendrerit in</text><text x="24" y="170">vulputate velit esse molestie consequat.</text>
    <text x="24" y="186">vel illum dolore eu feugiat nulla facilisis</text><text x="24" y="192">at vero eros et accumsan et iusto odio</text><text x="24" y="198">dignissim qui blandit praesent</text>
  </g>
  <rect x="171" y="45" width="320" height="130" fill="url(#photo-grey)" role="img" aria-label="Humanoid robot touching holographic screen"/>
  <rect x="214" y="137" width="86" height="27" class="fill-purple"/><text x="257" y="155" text-anchor="middle" font-size="9" font-weight="600" class="w">Text Here</text>
  <rect x="214" y="164" width="86" height="78" class="fill-white"/>
  <rect x="332" y="137" width="86" height="27" class="fill-purple"/><text x="375" y="155" text-anchor="middle" font-size="9" font-weight="600" class="w">Text Here</text>
  <rect x="332" y="164" width="86" height="78" class="fill-white"/>
  <g class="fine">
    <text x="220" y="174">Lorem ipsum dolor sit amet,</text><text x="220" y="180">consectetuer adipiscing elit,</text><text x="220" y="186">sed diam nonummy nibh</text><text x="220" y="192">euismod tincidunt ut laoreet</text><text x="220" y="204">Ut wisi enim ad minim</text><text x="220" y="210">veniam, quis nostrud exerci</text><text x="220" y="216">commodo conse</text>
    <text x="338" y="174">Lorem ipsum dolor sit amet,</text><text x="338" y="180">consectetuer adipiscing elit,</text><text x="338" y="186">sed diam nonummy nibh</text><text x="338" y="192">euismod tincidunt ut laoreet</text><text x="338" y="204">Ut wisi enim ad minim</text><text x="338" y="210">veniam, quis nostrud exerci</text><text x="338" y="216">commodo conse</text>
  </g>
  <rect x="10" y="253" width="7" height="7" class="fill-purple"/><text x="20" y="259" class="brand-sm">KINETRA</text>
  <line x1="50" y1="261" x2="480" y2="261" class="rule"/><text x="478" y="270" class="pg" text-anchor="end">3</text>
</svg>

<!-- 5 Process -->
<svg class="slide" viewBox="0 0 491 276">
  <text x="20" y="28" class="h2">Text Added Hare</text><rect x="20" y="36" width="14" height="2" class="fill-purple"/><rect x="36" y="36" width="4" height="2" class="fill-ink"/>
  <rect x="70" y="45" width="350" height="140" fill="#f1f1f3" role="img" aria-label="Faint world map background"/>
  <g stroke-width="3" class="stroke-ink">
    <rect x="92" y="66" width="80" height="124" rx="8"/>
    <rect x="205" y="66" width="80" height="124" rx="8"/>
    <rect x="318" y="66" width="80" height="124" rx="8"/>
  </g>
  <g class="fill-ink"><circle cx="172" cy="98" r="4"/><circle cx="205" cy="158" r="4"/><circle cx="285" cy="98" r="4"/><circle cx="318" cy="158" r="4"/></g>
  <g class="stroke-purple" stroke-width="1.5">
    <circle cx="132" cy="96" r="6"/><rect x="141" y="90" width="0" height="0"/>
    <rect x="238" y="91" width="14" height="10"/><polyline points="238,91 245,97 252,91"/>
    <polyline points="351,90 351,102 363,102"/><line x1="352" y1="101" x2="362" y2="91"/>
  </g>
  <text x="132" y="119" text-anchor="middle" class="label">IDEA</text>
  <text x="245" y="119" text-anchor="middle" class="label">PROMOTION</text>
  <text x="358" y="119" text-anchor="middle" class="label">GROWTH</text>
  <g class="fine" text-anchor="middle">
    <text x="132" y="129">Lorem ipsum dolor sit amet,</text><text x="132" y="135">consectetuer adipiscing elit,</text><text x="132" y="141">sed diam nonummy nibh</text><text x="132" y="147">euismod tincidunt ut</text><text x="132" y="153">laoreet dolore magna</text><text x="132" y="159">aliquam erat volutpat.</text><text x="132" y="165">nisl ut aliquip ex ea</text>
    <text x="245" y="129">Lorem ipsum dolor sit amet,</text><text x="245" y="135">consectetuer adipiscing elit,</text><text x="245" y="141">sed diam nonummy nibh</text><text x="245" y="147">euismod tincidunt ut</text><text x="245" y="153">laoreet dolore magna</text><text x="245" y="159">aliquam erat volutpat.</text><text x="245" y="165">nisl ut aliquip ex ea</text>
    <text x="358" y="129">Lorem ipsum dolor sit amet,</text><text x="358" y="135">consectetuer adipiscing elit,</text><text x="358" y="141">sed diam nonummy nibh</text><text x="358" y="147">euismod tincidunt ut</text><text x="358" y="153">laoreet dolore magna</text><text x="358" y="159">aliquam erat volutpat.</text><text x="358" y="165">nisl ut aliquip ex ea</text>
    <text x="245" y="219">Lorem ipsum dolor sit amet, consectetuer adipiscing elit, sed diam nonummy nibh euismod tincidunt ut laoreet dolore</text>
    <text x="245" y="225">magna aliquam erat volutpat. Ut wisi enim ad minim veniam, quis nostrud exerci tation ullamcorper suscipit lobortis nisl ut</text>
    <text x="245" y="231">aliquip ex ea commodo consequat. Duis autem vel eum iriure dolor in hendrerit</text>
  </g>
  <rect x="10" y="253" width="7" height="7" class="fill-purple"/><text x="20" y="259" class="brand-sm">KINETRA</text>
  <line x1="50" y1="261" x2="480" y2="261" class="rule"/><text x="478" y="270" class="pg" text-anchor="end">4</text>
</svg>

<!-- 6 Six columns -->
<svg class="slide" viewBox="0 0 491 276">
  <text x="20" y="28" class="h2">Text Added Hare</text><rect x="20" y="36" width="14" height="2" class="fill-purple"/><rect x="36" y="36" width="4" height="2" class="fill-ink"/>
  <g font-size="5.5" font-weight="600">
    <text x="38" y="73" class="fill-ink">1. Text Added Here</text><text x="186" y="73" class="p">1. Text Added Here</text><text x="329" y="73" class="fill-ink">1. Text Added Here</text>
    <text x="38" y="163" class="p">1. Text Added Here</text><text x="186" y="163" class="fill-ink">1. Text Added Here</text><text x="329" y="163" class="p">1. Text Added Here</text>
  </g>
  <g class="fine">
    <text x="38" y="82">Lorem ipsum dolor sit amet, cons ectetuer</text><text x="38" y="88">adipiscing elit, sed diam nonummy nibh</text><text x="38" y="94">euismod tincidunt ut laoreet dolore magna</text><text x="38" y="100">aliquam erat volutpat. Ut wisi enim ad</text><text x="38" y="112">Lorem ipsum dolor sit amet, consectetuer</text><text x="38" y="118">sed diam nonummy nibh euismod tincidunt</text>
    <text x="186" y="82">Lorem ipsum dolor sit amet, cons ectetuer</text><text x="186" y="88">adipiscing elit, sed diam nonummy nibh</text><text x="186" y="94">euismod tincidunt ut laoreet dolore magna</text><text x="186" y="100">aliquam erat volutpat. Ut wisi enim ad</text><text x="186" y="112">Lorem ipsum dolor sit amet, consectetuer</text><text x="186" y="118">sed diam nonummy nibh euismod tincidunt</text>
    <text x="329" y="82">Lorem ipsum dolor sit amet, cons ectetuer</text><text x="329" y="88">adipiscing elit, sed diam nonummy nibh</text><text x="329" y="94">euismod tincidunt ut laoreet dolore magna</text><text x="329" y="106">Lorem ipsum dolor sit amet, consectetuer</text><text x="329" y="112">sed diam nonummy nibh euismod tincidunt</text><text x="329" y="118">exerci tation ullamcorper suscipit</text>
    <text x="38" y="172">Lorem ipsum dolor sit amet, cons ectetuer</text><text x="38" y="178">adipiscing elit, sed diam nonummy nibh</text><text x="38" y="184">euismod tincidunt ut laoreet dolore magna</text><text x="38" y="196">Lorem ipsum dolor sit amet, consectetuer</text><text x="38" y="202">wisi enim ad minim veniam, quis nostrud</text><text x="38" y="208">ullamcorper suscipit lobortis nisl ut</text>
    <text x="186" y="172">Lorem ipsum dolor sit amet, cons ectetuer</text><text x="186" y="178">adipiscing elit, sed diam nonummy nibh</text><text x="186" y="184">euismod tincidunt ut laoreet dolore magna</text><text x="186" y="196">Lorem ipsum dolor sit amet, consectetuer</text><text x="186" y="202">sed diam nonummy nibh euismod tincidunt</text><text x="186" y="208">aliquip ex ea commodo consequat.</text>
    <text x="329" y="172">Lorem ipsum dolor sit amet, cons ectetuer</text><text x="329" y="178">adipiscing elit, sed diam nonummy nibh</text><text x="329" y="184">euismod tincidunt ut laoreet dolore magna</text><text x="329" y="196">Lorem ipsum dolor sit amet, consectetuer</text><text x="329" y="202">sed diam nonummy nibh euismod tincidunt</text><text x="329" y="208">ullamcorper suscipit lobortis nisl ut</text>
  </g>
  <rect x="10" y="253" width="7" height="7" class="fill-purple"/><text x="20" y="259" class="brand-sm">KINETRA</text>
  <line x1="50" y1="261" x2="480" y2="261" class="rule"/><text x="478" y="270" class="pg" text-anchor="end">5</text>
</svg>

<!-- 7 Market chart -->
<svg class="slide" viewBox="0 0 491 276">
  <text x="17" y="36" font-size="14" font-weight="700" class="fill-ink">Market</text>
  <text x="17" y="55" font-size="14" font-weight="700" class="fill-ink">Opportunities.</text>
  <rect x="17" y="70" width="14" height="2" class="fill-purple"/><rect x="33" y="70" width="4" height="2" class="fill-ink"/>
  <g class="fine" font-size="5">
    <text x="22" y="94">Lorem ipsum dolor sit amet,</text><text x="22" y="101">consectetuer adipiscing elit,</text><text x="22" y="108">sed diam nonummy nibh</text><text x="22" y="115">euismod tincidunt ut laoreet</text><text x="22" y="122">dolore magna aliquam erat</text><text x="22" y="129">volutpat. Ut wisi enim ad</text><text x="22" y="136">minim veniam, quis nostrud</text><text x="22" y="143">exerci tation ullamcorper</text><text x="22" y="150">suscipit lobortis et,</text>
    <text x="22" y="202">consectetuer adipiscing elit,</text><text x="22" y="209">sed diam nonummy nibh .</text>
  </g>
  <text x="203" y="39" font-size="5.5" font-weight="500" class="fill-ink">CONSECTETUER ADIPISCING</text>
  <g class="rule"><line x1="215" y1="55" x2="455" y2="55"/><line x1="215" y1="73" x2="455" y2="73"/><line x1="215" y1="92" x2="455" y2="92"/><line x1="215" y1="111" x2="455" y2="111"/><line x1="215" y1="130" x2="455" y2="130"/><line x1="215" y1="148" x2="455" y2="148"/><line x1="215" y1="167" x2="455" y2="167"/><line x1="455" y1="55" x2="455" y2="167"/></g>
  <g font-size="5" class="fill-ink" text-anchor="end">
    <text x="209" y="57">60</text><text x="209" y="75">50</text><text x="209" y="94">40</text><text x="209" y="113">30</text><text x="209" y="132">20</text><text x="209" y="150">10</text><text x="209" y="169">0</text>
  </g>
  <rect x="236" y="65" width="26" height="102" class="fill-purple"/>
  <rect x="288" y="106" width="26" height="61" class="fill-ink"/>
  <rect x="340" y="79" width="26" height="88" class="fill-purple"/>
  <rect x="392" y="116" width="26" height="51" class="fill-ink"/>
  <g font-size="5" class="fill-ink" text-anchor="middle"><text x="249" y="180">JAN</text><text x="301" y="180">FEB</text><text x="353" y="180">MAR</text><text x="405" y="180">APR</text></g>
  <circle cx="203" cy="204" r="2.5" class="fill-purple"/><text x="212" y="206" font-size="6" font-weight="600" class="fill-ink">Lorem Ipsum</text>
  <circle cx="337" cy="204" r="2.5" class="fill-purple"/><text x="346" y="206" font-size="6" font-weight="600" class="fill-ink">Lorem Ipsum</text>
  <g class="fine"><text x="212" y="214">Lorem ipsum dolor sit amet, consectetuer</text><text x="212" y="219">adipiscing elit, sed diam nonummy nibh</text><text x="212" y="224">euismod tincidunt ut laoreet</text>
  <text x="346" y="214">Lorem ipsum dolor sit amet, consectetuer</text><text x="346" y="219">adipiscing elit, sed diam nonummy nibh</text><text x="346" y="224">euismod tincidunt ut laoreet</text></g>
  <rect x="10" y="253" width="7" height="7" class="fill-purple"/><text x="20" y="259" class="brand-sm">KINETRA</text>
  <line x1="50" y1="261" x2="480" y2="261" class="rule"/><text x="478" y="270" class="pg" text-anchor="end">6</text>
</svg>

<!-- 8 Section break -->
<svg class="slide" viewBox="0 0 491 276">
  <rect x="22" y="17" width="447" height="242" fill="url(#photo-dark)" role="img" aria-label="Dark robotics workshop photo"/>
  <rect x="88" y="118" width="16" height="16" class="fill-purple"/>
  <text x="196" y="116" font-size="22" font-weight="500" class="w">Section</text>
  <text x="196" y="142" font-size="22" font-weight="700" class="p">Break</text>
  <g class="fine-w" font-size="5"><text x="196" y="158">Lorem ipsum dolor sit amet, consectetuer adipiscing elit</text><text x="196" y="165">sed diam nonummy nibh</text><text x="196" y="172">euismod tincid</text></g>
</svg>

<!-- 9 Hexagon -->
<svg class="slide" viewBox="0 0 491 276">
  <text x="20" y="28" class="h2">Text Added Hare</text><rect x="20" y="36" width="14" height="2" class="fill-purple"/><rect x="36" y="36" width="4" height="2" class="fill-ink"/>
  <polygon points="110,66 183,106 183,188 110,228 37,188 37,106" class="stroke-purple" stroke-width="1.5"/>
  <polygon points="110,74 176,111 176,183 110,220 44,183 44,111" fill="url(#photo-grey)" role="img" aria-label="Robotic gears and circuitry photo"/>
  <polygon points="175,67 200,81 200,108 175,122 150,108 150,81" fill="url(#photo-light)" role="img" aria-label="Circuit board close-up photo"/>
  <text x="231" y="68" font-size="7.5" font-weight="700" class="p">1. Text</text><text x="231" y="80" font-size="7.5" font-weight="700" class="fill-ink">Added Here</text>
  <g class="fine"><text x="231" y="90">Lorem ipsum dolor sit amet, cons ectetuer adipiscing elit, sed</text><text x="231" y="95">diam nonummy nibh euismod tincidunt ut laoreet dolore magna</text><text x="231" y="100">aliquam erat volutpat.</text><text x="231" y="108">Ut wisi enim ad minim veniam, quis nostrud exerci tation</text><text x="231" y="113">ullamcorper suscipit lobortis nisl ut aliquip ex ea commodo</text><text x="231" y="118">consequat. Lorem ipsum dolor sit amet, consectetuer adipiscing</text></g>
  <text x="231" y="164" font-size="7.5" font-weight="700" class="p">2. Text</text><text x="231" y="176" font-size="7.5" font-weight="700" class="fill-ink">Added Here</text>
  <g class="fine"><text x="231" y="186">Lorem ipsum dolor sit amet, cons ectetuer adipiscing elit, sed</text><text x="231" y="191">diam nonummy nibh euismod tincidunt ut laoreet dolore magna</text><text x="231" y="196">aliquam erat volutpat.</text><text x="231" y="204">Ut wisi enim ad minim veniam, quis nostrud exerci tation</text><text x="231" y="209">ullamcorper suscipit lobortis nisl ut aliquip ex ea commodo</text><text x="231" y="214">consequat. Lorem ipsum dolor sit amet, consectetuer adipiscing</text></g>
  <rect x="10" y="253" width="7" height="7" class="fill-purple"/><text x="20" y="259" class="brand-sm">KINETRA</text>
  <line x1="50" y1="261" x2="480" y2="261" class="rule"/><text x="478" y="270" class="pg" text-anchor="end">8</text>
</svg>

<!-- 10 List + dark panel -->
<svg class="slide" viewBox="0 0 491 276">
  <text x="20" y="28" class="h2">Text Added Hare</text><rect x="20" y="36" width="14" height="2" class="fill-purple"/><rect x="36" y="36" width="4" height="2" class="fill-ink"/>
  <g font-size="5" font-weight="600">
    <text x="52" y="73"><tspan class="p">01.</tspan> <tspan class="fill-ink">Aliquam Erat Volutpat</tspan></text>
    <text x="52" y="117"><tspan class="p">02.</tspan> <tspan class="fill-ink">Consectetuer Adipiscing Elit</tspan></text>
    <text x="52" y="163"><tspan class="p">03.</tspan> <tspan class="fill-ink">Duis Autem Vel Eum</tspan></text>
    <text x="52" y="206"><tspan class="p">04.</tspan> <tspan class="fill-ink">Aliquam Erat Volutpat</tspan></text>
  </g>
  <g class="fine">
    <text x="66" y="80">Lorem ipsum dolor sit amet, consectetuer adipiscing elit,</text><text x="66" y="85">sed diam nonummy nibh euismod</text>
    <text x="66" y="124">Lorem ipsum dolor sit amet, consectetuer adipiscing elit,</text><text x="66" y="129">sed diam nonummy nibh euismod tincidunt ut laoreet</text>
    <text x="66" y="170">Lorem ipsum dolor sit amet, consectetuer adipiscing elit,</text><text x="66" y="175">sed diam nonummy nibh euismod tincidunt.</text>
    <text x="66" y="213">Lorem ipsum dolor sit amet, consectetuer adipiscing elit,</text><text x="66" y="218">sed diam nonummy nibh euismod tincidunt ut laoreet</text>
  </g>
  <rect x="266" y="59" width="168" height="171" class="fill-dark"/>
  <g class="fill-purple" stroke="#fff" stroke-width="2"><circle cx="266" cy="92" r="15"/><circle cx="266" cy="145" r="15"/><circle cx="266" cy="198" r="15"/></g>
  <g class="stroke-ink" stroke="#fff" stroke-width="1.2">
    <rect x="259" y="86" width="14" height="10"/><line x1="266" y1="96" x2="266" y2="100"/>
    <path d="M259 146 a7 5 0 0 1 14 0 z"/><line x1="266" y1="146" x2="266" y2="152"/>
    <polyline points="258,203 263,195 269,199 274,191"/>
  </g>
  <text x="295" y="87" font-size="7" font-weight="600" class="w">Lorem ipsum</text>
  <text x="295" y="140" font-size="7" font-weight="600" class="w">Lorem ipsum</text>
  <text x="295" y="193" font-size="7" font-weight="600" class="w">Lorem ipsum</text>
  <g class="fine-w">
    <text x="295" y="95">Lorem ipsum dolor sit amet, cons ectetuer</text><text x="295" y="100">adipiscing elit, sed diam nonummy</text><text x="295" y="105">nibh euismod tincidunt ut laoreet</text>
    <text x="295" y="148">Lorem ipsum dolor sit amet, cons ectetuer</text><text x="295" y="153">adipiscing elit, sed diam nonummy</text><text x="295" y="158">nibh euismod tincidunt ut laoreet</text>
    <text x="295" y="201">Lorem ipsum dolor sit amet, cons ectetuer</text><text x="295" y="206">adipiscing elit, sed diam nonummy</text><text x="295" y="211">nibh euismod tincidunt</text>
  </g>
  <rect x="10" y="253" width="7" height="7" class="fill-purple"/><text x="20" y="259" class="brand-sm">KINETRA</text>
  <line x1="50" y1="261" x2="480" y2="261" class="rule"/><text x="478" y="265" class="pg" text-anchor="end">9</text>
</svg>

<!-- 11 Values -->
<svg class="slide" viewBox="0 0 491 276">
  <text x="20" y="28" class="h2">Text Added Hare</text><rect x="20" y="36" width="14" height="2" class="fill-purple"/><rect x="36" y="36" width="4" height="2" class="fill-ink"/>
  <g class="fine" font-size="5.5">
    <text x="25" y="73">Lorem ipsum dolor</text><text x="25" y="80">sit amet,consectetuer</text><text x="25" y="87">adipiscing elit, sed</text><text x="25" y="94">diam nonummy nibh</text><text x="25" y="101">euismod tincidunt</text><text x="25" y="108">erat volutpat.</text>
    <text x="25" y="122">Ut wisi enim ad</text><text x="25" y="129">minim veniam, quis</text><text x="25" y="136">nostrud exerci tation</text><text x="25" y="143">ullamcorper suscipit</text><text x="25" y="150">lobortis nisl ut aliquip</text><text x="25" y="157">ex ea commodo</text><text x="25" y="164">consequat.</text>
  </g>
  <polygon points="205,33 295,33 240,238 120,238 170,176" fill="url(#photo-grey)" role="img" aria-label="Business people silhouettes in office"/>
  <polygon points="130,180 170,180 150,238 120,238" class="fill-purple" opacity=".85"/>
  <g class="fill-purple" stroke="#fff" stroke-width="2"><circle cx="280" cy="78" r="16"/><circle cx="254" cy="145" r="16"/><circle cx="224" cy="206" r="16"/></g>
  <g fill="#fff"><circle cx="276" cy="76" r="3"/><circle cx="284" cy="76" r="3"/><rect x="271" y="80" width="18" height="5" rx="2"/><circle cx="251" cy="141" r="2.5"/><circle cx="258" cy="141" r="2.5"/><rect x="249" y="144" width="11" height="8"/><path d="M224 212 l-6-6 a3.5 3.5 0 0 1 6-4 a3.5 3.5 0 0 1 6 4 z"/></g>
  <text x="314" y="73" font-size="7" font-weight="700" class="fill-ink">We Before Me</text>
  <text x="287" y="140" font-size="7" font-weight="700" class="fill-ink">We Are Good People</text>
  <text x="254" y="205" font-size="7" font-weight="700" class="fill-ink">We Work with Heart</text>
  <g class="fine">
    <text x="314" y="81">ipsum dolor sit amet, cons ectetuer adipiscing</text><text x="314" y="86">elit, sed diam nonummy nibh euismod tincidunt</text><text x="314" y="91">ut laoreet</text>
    <text x="287" y="148">ipsum dolor sit amet, cons ectetuer adipiscing elit,</text><text x="287" y="153">sed diam nonummy nibh euismod tincidunt ut</text><text x="287" y="158">laoreet dolore magna aliquam erat volutpat.</text>
    <text x="254" y="214">ipsum dolor sit amet, cons ectetuer adipiscing</text><text x="254" y="219">elit, sed diam nonummy nibh euismod tincidunt</text>
  </g>
  <rect x="10" y="253" width="7" height="7" class="fill-purple"/><text x="20" y="259" class="brand-sm">KINETRA</text>
  <line x1="50" y1="261" x2="480" y2="261" class="rule"/><text x="478" y="265" class="pg" text-anchor="end">10</text>
</svg>

<!-- 12 Cycle -->
<svg class="slide" viewBox="0 0 491 276">
  <text x="20" y="28" class="h2">Text Added Hare</text><rect x="20" y="36" width="14" height="2" class="fill-purple"/><rect x="36" y="36" width="4" height="2" class="fill-ink"/>
  <g class="fine">
    <text x="23" y="60">Lorem ipsum dolor sit amet, consectetuer</text><text x="23" y="66">adipiscing elit, sed diam nonummy nibh</text>
    <text x="23" y="78">Ut wisi enim ad minim veniam, quis</text><text x="23" y="84">nostrud exerci tation ullamcorper suscipit</text><text x="23" y="90">lobortis. Ut wisi enim ad minim veniam, quis</text><text x="23" y="96">nostrud exerci tation ullamcorper suscipit</text><text x="23" y="102">lobortis. Ut wisi enim ad minim veniam, quis</text><text x="23" y="108">nostrud exerci tation ullamcorper suscipit</text><text x="23" y="114">lobortis.</text>
    <text x="49" y="170">Lorem ipsum dolor sit amet, consectetuer</text><text x="49" y="175">adipiscing elit, sed diam nonummy nibh</text>
    <text x="49" y="204">Lorem ipsum dolor sit amet, consectetuer</text><text x="49" y="209">adipiscing elit, sed diam nonummy nibh</text>
  </g>
  <circle cx="40" cy="162" r="2.5" class="fill-purple"/><text x="49" y="163" font-size="5.5" font-weight="600" class="fill-ink">Lorem ipsum</text>
  <circle cx="40" cy="196" r="2.5" class="fill-purple"/><text x="49" y="197" font-size="5.5" font-weight="600" class="fill-ink">Lorem ipsum</text>
  <path d="M224 125 A90 88 0 1 1 312 220" class="stroke-ink" stroke-width="5"/>
  <polyline points="216,114 224,130 234,116" class="stroke-ink" stroke-width="4"/>
  <g class="fill-purple"><circle cx="372" cy="84" r="19"/><circle cx="390" cy="160" r="16"/><circle cx="350" cy="210" r="13"/><circle cx="248" cy="188" r="11"/></g>
  <g fill="#fff"><circle cx="372" cy="84" r="12"/><circle cx="390" cy="160" r="10"/><circle cx="350" cy="210" r="8"/><circle cx="248" cy="188" r="7"/></g>
  <g class="fill-purple"><circle cx="372" cy="84" r="5"/><circle cx="390" cy="160" r="4"/><circle cx="350" cy="210" r="3"/><circle cx="248" cy="188" r="3"/></g>
  <g class="fill-purple"><rect x="272" y="110" width="3" height="12"/><rect x="277" y="114" width="3" height="8"/><rect x="282" y="106" width="3" height="16"/></g>
  <text x="282" y="131" text-anchor="middle" font-size="6" font-weight="700" class="fill-ink">MAIN TITLE</text>
  <g class="fine" font-size="3.5" text-anchor="middle"><text x="282" y="137">Lorem ipsum dolor sit amet,</text><text x="282" y="141">consectetuer adipiscing elit,</text><text x="282" y="145">sed diam nonummy nibh</text></g>
  <g font-size="4" class="p"><text x="412" y="62">85%</text><text x="336" y="142">80%</text><text x="285" y="186">50%</text><text x="385" y="227">75%</text></g>
  <g font-size="5.5" font-weight="600" class="fill-ink"><text x="420" y="75">Your Title</text><text x="431" y="145">Your Title</text><text x="186" y="189">Your Title</text><text x="410" y="205">Your Title</text></g>
  <g class="fine" font-size="3.3"><text x="420" y="81">Lorem ipsum dolor sit amet,</text><text x="420" y="85">consectetuer adipiscing elit,</text><text x="431" y="151">Lorem ipsum dolor sit amet,</text><text x="431" y="155">consectetuer adipiscing elit,</text><text x="180" y="195">Lorem ipsum dolor sit</text><text x="180" y="199">consectetuer adipiscing</text><text x="410" y="211">Lorem ipsum dolor sit amet,</text><text x="410" y="215">consectetuer adipiscing elit,</text></g>
  <rect x="10" y="253" width="7" height="7" class="fill-purple"/><text x="20" y="259" class="brand-sm">KINETRA</text>
  <line x1="50" y1="261" x2="480" y2="261" class="rule"/><text x="478" y="265" class="pg" text-anchor="end">11</text>
</svg>

<!-- 13 Hub -->
<svg class="slide" viewBox="0 0 491 276">
  <text x="20" y="28" class="h2">Text Added Hare</text><rect x="20" y="36" width="14" height="2" class="fill-purple"/><rect x="36" y="36" width="4" height="2" class="fill-ink"/>
  <circle cx="111" cy="139" r="59" class="fill-purple"/><circle cx="111" cy="139" r="55" fill="#fff"/><circle cx="111" cy="139" r="52" class="fill-ink"/><circle cx="111" cy="139" r="47" fill="#fff"/>
  <text x="111" y="142" text-anchor="middle" font-size="9" font-weight="700" class="fill-ink">KINETRA</text>
  <polyline points="173,102 193,77 232,77" class="stroke-ink" stroke-width="1.2"/>
  <line x1="181" y1="139" x2="232" y2="139" class="stroke-ink" stroke-width="1.2"/>
  <polyline points="173,176 193,201 232,201" class="stroke-ink" stroke-width="1.2"/>
  <g class="fill-purple"><circle cx="264" cy="75" r="19"/><circle cx="264" cy="139" r="19"/><circle cx="264" cy="200" r="19"/></g>
  <g stroke="#fff" fill="none" stroke-width="1.3"><circle cx="264" cy="75" r="7"/><circle cx="264" cy="75" r="3"/><circle cx="264" cy="139" r="7"/><circle cx="264" cy="139" r="3"/><circle cx="264" cy="200" r="7"/><circle cx="264" cy="200" r="3"/></g>
  <g font-size="7" font-weight="600" class="fill-ink"><text x="295" y="66">Project name</text><text x="295" y="128">Project name</text><text x="295" y="193">Project name</text></g>
  <g class="fine">
    <text x="295" y="73">Lorem ipsum dolor sit amet, nec an dictas equidem</text><text x="295" y="78">appellantur, ut has commune accommodare. Mea</text><text x="295" y="83">illum, ludus solet idpro.</text>
    <text x="295" y="135">Lorem ipsum dolor sit amet, nec an dictas equidem</text><text x="295" y="140">appellantur, ut has commune accommodare. Mea</text><text x="295" y="145">illum, ludus solet idpro.</text>
    <text x="295" y="200">Lorem ipsum dolor sit amet, nec an dictas equidem</text><text x="295" y="205">appellantur, ut has commune accommodare. Mea</text><text x="295" y="210">illum, ludus solet idpro.</text>
  </g>
  <rect x="10" y="253" width="7" height="7" class="fill-purple"/><text x="20" y="259" class="brand-sm">KINETRA</text>
  <line x1="50" y1="261" x2="480" y2="261" class="rule"/><text x="478" y="265" class="pg" text-anchor="end">12</text>
</svg>

<!-- 14 Options -->
<svg class="slide" viewBox="0 0 491 276">
  <text x="20" y="28" class="h2">Text Added Hare</text><rect x="20" y="36" width="14" height="2" class="fill-purple"/><rect x="36" y="36" width="4" height="2" class="fill-ink"/>
  <polygon points="30,120 56,120 84,149 56,178 30,178 58,149" fill="#e8e8ea"/>
  <rect x="117" y="58" width="93" height="110" fill="url(#photo-dark)" role="img" aria-label="Business growth arrows photo"/>
  <rect x="237" y="58" width="93" height="110" fill="url(#photo-grey)" role="img" aria-label="Digital document interface photo"/>
  <rect x="357" y="58" width="93" height="110" fill="url(#photo-grey)" role="img" aria-label="Team working at laptop photo"/>
  <g font-size="7" font-weight="600"><text x="117" y="183"><tspan class="p">First</tspan> <tspan class="fill-ink">Option</tspan></text><text x="237" y="182"><tspan class="p">Second</tspan> <tspan class="fill-ink">Option</tspan></text><text x="357" y="183"><tspan class="p">Third</tspan> <tspan class="fill-ink">Option</tspan></text></g>
  <g class="fine">
    <text x="117" y="192">Lorem ipsum dolor sit</text><text x="117" y="197">consectetuer adipiscing elit,</text><text x="117" y="202">sed diam nonummy nibh</text><text x="117" y="207">euismod tincidunt ut dolore</text><text x="117" y="212">magna aliquam erat</text><text x="117" y="217">volutpat. Ut wisi enim ad</text><text x="117" y="222">minim veniam, quis nostrud</text>
    <text x="237" y="192">Lorem ipsum dolor sit</text><text x="237" y="197">consectetuer adipiscing elit,</text><text x="237" y="202">sed diam nonummy nibh</text><text x="237" y="207">euismod tincidunt ut dolore</text><text x="237" y="212">magna aliquam erat</text><text x="237" y="217">volutpat. Ut wisi enim ad</text><text x="237" y="222">minim veniam, quis nostrud</text>
    <text x="357" y="192">Lorem ipsum dolor sit</text><text x="357" y="197">consectetuer adipiscing elit,</text><text x="357" y="202">sed diam nonummy nibh</text><text x="357" y="207">euismod tincidunt ut dolore</text><text x="357" y="212">magna aliquam erat</text><text x="357" y="217">volutpat. Ut wisi enim ad</text><text x="357" y="222">minim veniam, quis nostrud</text>
  </g>
  <rect x="10" y="253" width="7" height="7" class="fill-purple"/><text x="20" y="259" class="brand-sm">KINETRA</text>
  <line x1="50" y1="261" x2="480" y2="261" class="rule"/><text x="478" y="265" class="pg" text-anchor="end">13</text>
</svg>

<!-- 15 Icon grid -->
<svg class="slide" viewBox="0 0 491 276">
  <text x="20" y="28" class="h2">Text Added Hare</text><rect x="20" y="36" width="14" height="2" class="fill-purple"/><rect x="36" y="36" width="4" height="2" class="fill-ink"/>
  <g stroke-width="1.5">
    <rect x="95" y="57" width="33" height="33" class="fill-purple"/><rect x="228" y="57" width="33" height="33" class="fill-ink"/><rect x="360" y="57" width="33" height="33" class="fill-purple"/>
    <rect x="95" y="150" width="33" height="33" class="fill-ink"/><rect x="228" y="150" width="33" height="33" class="fill-purple"/><rect x="360" y="150" width="33" height="33" class="fill-ink"/>
  </g>
  <g stroke="#fff" fill="none" stroke-width="1.2">
    <rect x="98" y="60" width="27" height="27"/><circle cx="107" cy="71" r="3"/><circle cx="116" cy="71" r="3"/><path d="M102 82 q5-6 10 0 q5-6 10 0"/>
    <rect x="231" y="60" width="27" height="27"/><circle cx="240" cy="70" r="4"/><circle cx="249" cy="77" r="4"/>
    <rect x="363" y="60" width="27" height="27"/><polyline points="368,82 368,76 373,76 373,82 378,82 378,72 383,72 383,82"/><polyline points="368,70 376,66 384,64"/>
    <rect x="98" y="153" width="27" height="27"/><polyline points="103,158 103,176 121,176"/><path d="M106 160 q4 12 14 13"/>
    <rect x="231" y="153" width="27" height="27"/><path d="M240 162 h9 l3 12 h-15 z"/><line x1="244" y1="158" x2="245" y2="162"/>
    <rect x="363" y="153" width="27" height="27"/><circle cx="376" cy="165" r="6"/><polyline points="372,170 370,177 376,174 382,177 380,170"/>
  </g>
  <g font-size="6" font-weight="600" text-anchor="middle"><text x="112" y="102" class="fill-ink">Lorem ipsum</text><text x="245" y="102" class="p">Lorem ipsum</text><text x="377" y="102" class="fill-ink">Lorem ipsum</text><text x="112" y="195" class="p">Lorem ipsum</text><text x="245" y="195" class="fill-ink">Lorem ipsum</text><text x="377" y="195" class="p">Lorem ipsum</text></g>
  <g class="fine" text-anchor="middle">
    <text x="112" y="109">Lorem ipsum dolor sit amet,</text><text x="112" y="114">consectetuer adipiscing elit, sed</text><text x="112" y="119">diam nonummy nibh euismod</text><text x="112" y="124">tincidunt ut laoreet</text>
    <text x="245" y="109">Lorem ipsum dolor sit amet,</text><text x="245" y="114">consectetuer adipiscing elit, sed</text><text x="245" y="119">diam nonummy nibh euismod</text><text x="245" y="124">tincidunt ut laoreet</text>
    <text x="377" y="109">Lorem ipsum dolor sit amet,</text><text x="377" y="114">consectetuer adipiscing elit, sed</text><text x="377" y="119">diam nonummy nibh euismod</text><text x="377" y="124">tincidunt ut laoreet</text>
    <text x="112" y="202">Lorem ipsum dolor sit amet,</text><text x="112" y="207">consectetuer adipiscing elit, sed</text><text x="112" y="212">diam nonummy nibh euismod</text><text x="112" y="217">tincidunt ut laoreet</text>
    <text x="245" y="202">Lorem ipsum dolor sit amet,</text><text x="245" y="207">consectetuer adipiscing elit, sed</text><text x="245" y="212">diam nonummy nibh euismod</text><text x="245" y="217">tincidunt ut laoreet</text>
    <text x="377" y="202">Lorem ipsum dolor sit amet,</text><text x="377" y="207">consectetuer adipiscing elit, sed</text><text x="377" y="212">diam nonummy nibh euismod</text><text x="377" y="217">tincidunt ut laoreet</text>
  </g>
  <rect x="10" y="253" width="7" height="7" class="fill-purple"/><text x="20" y="259" class="brand-sm">KINETRA</text>
  <line x1="50" y1="261" x2="480" y2="261" class="rule"/><text x="478" y="265" class="pg" text-anchor="end">14</text>
</svg>

<!-- 16 Timeline -->
<svg class="slide" viewBox="0 0 491 276">
  <text x="20" y="28" class="h2">Text Added Hare</text><rect x="20" y="36" width="14" height="2" class="fill-purple"/><rect x="36" y="36" width="4" height="2" class="fill-ink"/>
  <g>
    <polygon points="44,138 64,130 115,130 128,138 115,146 64,146" class="fill-ink"/>
    <polygon points="126,130 195,130 208,138 195,146 126,146 138,138" class="fill-purple"/>
    <polygon points="206,130 275,130 288,138 275,146 206,146 218,138" class="fill-ink"/>
    <polygon points="286,130 355,130 368,138 355,146 286,146 298,138" class="fill-purple"/>
    <polygon points="366,130 427,130 447,138 427,146 366,146 378,138" class="fill-ink"/>
  </g>
  <g font-size="5.5" font-weight="600" fill="#fff" text-anchor="middle"><text x="87" y="140">1990</text><text x="167" y="140">2001</text><text x="246" y="140">2007</text><text x="326" y="140">2012</text><text x="406" y="140">2020</text></g>
  <g class="stroke-ink" stroke-width="1.2"><line x1="87" y1="112" x2="87" y2="128"/><line x1="246" y1="112" x2="246" y2="128"/><line x1="406" y1="112" x2="406" y2="128"/></g>
  <g class="fill-ink"><circle cx="87" cy="111" r="2.5"/><circle cx="246" cy="111" r="2.5"/><circle cx="406" cy="111" r="2.5"/></g>
  <g class="stroke-purple" stroke-width="1.2"><line x1="167" y1="148" x2="167" y2="164"/><line x1="326" y1="148" x2="326" y2="164"/></g>
  <g class="fill-purple"><circle cx="167" cy="165" r="2.5"/><circle cx="326" cy="165" r="2.5"/></g>
  <g font-size="6" font-weight="600" class="fill-ink" text-anchor="middle"><text x="87" y="75">Your Title</text><text x="246" y="75">Your Title</text><text x="406" y="75">Your Title</text><text x="167" y="183">Your Title</text><text x="326" y="183">Your Title</text></g>
  <g class="fine" font-size="4.6" text-anchor="middle"><text x="87" y="82">Refers to a good or</text><text x="87" y="88">service being offered</text><text x="246" y="82">Refers to a good or</text><text x="246" y="88">service being offered</text><text x="406" y="82">Refers to a good or</text><text x="406" y="88">service being offered</text><text x="167" y="190">Refers to a good or</text><text x="167" y="196">service being offered</text><text x="326" y="190">Refers to a good or</text><text x="326" y="196">service being offered</text></g>
  <rect x="10" y="253" width="7" height="7" class="fill-purple"/><text x="20" y="259" class="brand-sm">KINETRA</text>
  <line x1="50" y1="261" x2="480" y2="261" class="rule"/><text x="478" y="265" class="pg" text-anchor="end">15</text>
</svg>

<!-- 17 Dark cards -->
<svg class="slide" viewBox="0 0 491 276">
  <text x="20" y="28" class="h2">Text Added Hare</text><rect x="20" y="36" width="14" height="2" class="fill-purple"/><rect x="36" y="36" width="4" height="2" class="fill-ink"/>
  <rect x="0" y="57" width="491" height="172" class="fill-dark"/>
  <g stroke="#fff" fill="none" stroke-width="1"><rect x="54" y="87" width="80" height="122"/><rect x="154" y="87" width="80" height="122"/><rect x="254" y="87" width="80" height="122"/><rect x="353" y="87" width="80" height="122"/></g>
  <g class="fill-purple"><circle cx="94" cy="85" r="13"/><circle cx="194" cy="85" r="13"/><circle cx="294" cy="85" r="13"/><circle cx="393" cy="85" r="13"/></g>
  <g stroke="#fff" fill="none" stroke-width="1.2"><rect x="88" y="80" width="12" height="10"/><rect x="188" y="80" width="12" height="9"/><polygon points="286,84 294,80 302,84 294,88"/><rect x="387" y="79" width="12" height="11"/></g>
  <g font-size="6.5" font-weight="600" class="p"><text x="66" y="118">Lorem ipsum</text><text x="166" y="118">Lorem ipsum</text><text x="266" y="118">Lorem ipsum</text><text x="365" y="116">Lorem ipsum</text></g>
  <g class="fine-w">
    <text x="66" y="126">Lorem ipsum dolor sit amet,</text><text x="66" y="131">cons ectetuer adipiscing</text><text x="66" y="136">elit, sed diam nonummy</text><text x="66" y="141">nibh euismod tincidunt</text><text x="66" y="146">ut laoreet</text><text x="66" y="158">ipsum dolor sit amet,</text><text x="66" y="163">cons ectetuer adipiscing</text><text x="66" y="168">elit, sed diam nonummy</text><text x="66" y="173">nibh euismod tincidunt</text><text x="66" y="178">ut laoreet ipsum dolor sit</text><text x="66" y="183">amet, cons ectetuer</text>
    <text x="166" y="126">Lorem ipsum dolor sit amet,</text><text x="166" y="131">cons ectetuer adipiscing</text><text x="166" y="136">elit, sed diam nonummy</text><text x="166" y="141">nibh euismod tincidunt</text><text x="166" y="146">ut laoreet</text><text x="166" y="158">ipsum dolor sit amet,</text><text x="166" y="163">cons ectetuer adipiscing</text><text x="166" y="168">elit, sed diam nonummy</text><text x="166" y="173">nibh euismod tincidunt</text><text x="166" y="178">ut laoreet ipsum dolor sit</text><text x="166" y="183">amet, cons ectetuer</text>
    <text x="266" y="126">Lorem ipsum dolor sit amet,</text><text x="266" y="131">cons ectetuer adipiscing</text><text x="266" y="136">elit, sed diam nonummy</text><text x="266" y="141">nibh euismod tincidunt</text><text x="266" y="146">ut laoreet</text><text x="266" y="158">ipsum dolor sit amet,</text><text x="266" y="163">cons ectetuer adipiscing</text><text x="266" y="168">elit, sed diam nonummy</text><text x="266" y="173">nibh euismod tincidunt</text><text x="266" y="178">ut laoreet ipsum dolor sit</text><text x="266" y="183">amet, cons ectetuer</text>
    <text x="365" y="124">Lorem ipsum dolor sit amet,</text><text x="365" y="129">cons ectetuer adipiscing</text><text x="365" y="134">elit, sed diam nonummy</text><text x="365" y="139">nibh euismod tincidunt</text><text x="365" y="144">ut laoreet</text><text x="365" y="156">ipsum dolor sit amet,</text><text x="365" y="161">cons ectetuer adipiscing</text><text x="365" y="166">elit, sed diam nonummy</text><text x="365" y="171">nibh euismod tincidunt</text><text x="365" y="176">ut laoreet ipsum dolor sit</text><text x="365" y="181">amet, cons ectetuer</text>
  </g>
  <rect x="10" y="253" width="7" height="7" class="fill-purple"/><text x="20" y="259" class="brand-sm">KINETRA</text>
  <line x1="50" y1="261" x2="480" y2="261" class="rule"/><text x="478" y="265" class="pg" text-anchor="end">16</text>
</svg>

<!-- 18 Ring -->
<svg class="slide" viewBox="0 0 491 276">
  <text x="20" y="28" class="h2">Text Added Hare</text><rect x="20" y="36" width="14" height="2" class="fill-purple"/><rect x="36" y="36" width="4" height="2" class="fill-ink"/>
  <g transform="translate(247,145)">
    <path d="M0,-75 A75 75 0 0 1 75,0 L40,0 A40 40 0 0 0 0,-40 Z" class="fill-purple"/>
    <path d="M75,0 A75 75 0 0 1 0,75 L0,40 A40 40 0 0 0 40,0 Z" class="fill-ink"/>
    <path d="M0,75 A75 75 0 0 1 -75,0 L-40,0 A40 40 0 0 0 0,40 Z" class="fill-purple"/>
    <path d="M-75,0 A75 75 0 0 1 0,-75 L0,-40 A40 40 0 0 0 -40,0 Z" class="fill-ink"/>
    <g fill="#fff"><circle cx="0" cy="-57" r="6"/><circle cx="57" cy="0" r="6"/><circle cx="0" cy="57" r="6"/><circle cx="-57" cy="0" r="6"/></g>
    <g stroke="#fff" fill="none" stroke-width="1.3"><circle cx="-33" cy="-40" r="5"/><path d="M33 -44 l8 -8 M33 -44 l-3 6"/><circle cx="33" cy="40" r="5"/><rect x="-38" y="34" width="10" height="9"/></g>
    <text x="0" y="-2" text-anchor="middle" font-size="9" font-weight="700" class="fill-ink">Text</text>
    <text x="0" y="10" text-anchor="middle" font-size="9" font-weight="700" class="fill-ink">Added</text>
  </g>
  <g font-size="7" font-weight="600" class="fill-ink"><text x="150" y="78" text-anchor="end">Text Here</text><text x="327" y="78">Text Here</text><text x="150" y="185" text-anchor="end">Text Here</text><text x="327" y="185">Text Here</text></g>
  <g class="fine" font-size="4.6">
    <g text-anchor="end"><text x="150" y="86">Lorem ipsum dolor sit amet, consectetuer</text><text x="150" y="92">adipiscing elit, sed diammy nibh euismod</text><text x="150" y="98">tincidunt ut laoreet dolore</text><text x="150" y="193">Lorem ipsum dolor sit amet, consectetuer</text><text x="150" y="199">adipiscing elit, sed diammy nibh euismod</text><text x="150" y="205">tincidunt ut laoreet dolore</text></g>
    <text x="327" y="86">Lorem ipsum dolor sit amet, consectetuer</text><text x="327" y="92">adipiscing elit, sed diammy nibh euismod</text><text x="327" y="98">tincidunt ut laoreet dolore</text><text x="327" y="193">Lorem ipsum dolor sit amet, consectetuer</text><text x="327" y="199">adipiscing elit, sed diammy nibh euismod</text><text x="327" y="205">tincidunt ut laoreet dolore</text>
  </g>
  <rect x="10" y="253" width="7" height="7" class="fill-purple"/><text x="20" y="259" class="brand-sm">KINETRA</text>
  <line x1="50" y1="261" x2="480" y2="261" class="rule"/><text x="478" y="265" class="pg" text-anchor="end">17</text>
</svg>

<!-- 19 App screens -->
<svg class="slide" viewBox="0 0 491 276">
  <text x="20" y="28" class="h2">Text Added Hare</text><rect x="20" y="36" width="14" height="2" class="fill-purple"/><rect x="36" y="36" width="4" height="2" class="fill-ink"/>
  <g class="fine">
    <text x="26" y="60">Lorem ipsum dolor sit amet, consectetuer</text><text x="26" y="66">adipiscing elit, sed diam nonummy nibh euismod</text><text x="26" y="72">tincidunt ut laoreet dolore magna aliquam erat</text><text x="26" y="78">volutpat. Ut wisi enim ad minim veniam,</text>
    <text x="26" y="90">quis nostrud exerci tation ullamcorper suscipit</text><text x="26" y="96">lobortis nisl ut aliquip ex ea commodo consequat.</text><text x="26" y="102">Duis autem vel eum iriure dolor in hendrerit in</text><text x="26" y="108">vulputate velit esse</text>
    <text x="64" y="149">Lorem ipsum dolor sit amet, consectetuer adipiscing</text><text x="64" y="154">elit, sed diam nonummy nibh euismod tincid</text>
    <text x="64" y="183">Lorem ipsum dolor sit amet, consectetuer adipiscing</text><text x="64" y="188">elit, sed diam nonummy nibh euismod tincid</text>
    <text x="64" y="217">Lorem ipsum dolor sit amet, consectetuer adipiscing</text><text x="64" y="222">elit, sed diam nonummy nibh euismod tincid</text>
  </g>
  <g class="fill-purple"><rect x="43" y="133" width="14" height="14"/><rect x="43" y="167" width="14" height="14"/><rect x="43" y="201" width="14" height="14"/></g>
  <g font-size="7" font-weight="700" fill="#fff" text-anchor="middle"><text x="50" y="143">1.</text><text x="50" y="177">2.</text><text x="50" y="211">3.</text></g>
  <g font-size="6" font-weight="600" class="fill-ink"><text x="64" y="142">Lorem Ipsum</text><text x="64" y="176">Lorem Ipsum</text><text x="64" y="210">Lorem Ipsum</text></g>
  <rect x="330" y="55" width="130" height="180" fill="#f2f2f4" role="img" aria-label="Faint decorative pattern"/>
  <g class="stroke-ink" stroke-width="1.3">
    <rect x="228" y="37" width="55" height="128" rx="5" fill="#fff"/>
    <rect x="300" y="78" width="55" height="128" rx="5" fill="#fff"/>
    <rect x="374" y="118" width="55" height="128" rx="5" fill="#fff"/>
  </g>
  <g class="fill-ink"><rect x="246" y="39" width="18" height="3" rx="1"/><rect x="318" y="80" width="18" height="3" rx="1"/><rect x="392" y="120" width="18" height="3" rx="1"/></g>
  <g font-size="6" class="fill-ink"><text x="234" y="60">Lorem</text><text x="234" y="68">ipsum dolor</text><text x="306" y="108">Dolor sit</text><text x="306" y="116">amet, conse</text><text x="380" y="150">Consec</text></g>
  <g class="stroke-purple" stroke-width="1.2"><line x1="255" y1="80" x2="255" y2="92"/><circle cx="255" cy="78" r="3"/><circle cx="327" cy="130" r="6"/><circle cx="402" cy="172" r="7"/></g>
  <g class="fine" font-size="3.3">
    <text x="234" y="102">To introduce the</text><text x="234" y="106">students to the</text><text x="234" y="110">changing landscape of</text><text x="234" y="114">marketing and equip</text><text x="234" y="118">them with knowledge</text>
    <text x="306" y="150">You will learn concepts</text><text x="306" y="154">and ideas in digital</text><text x="306" y="158">marketing as well as</text><text x="306" y="162">how to use different</text>
    <text x="380" y="190">You are required to pass</text><text x="380" y="194">80% of the evaluation</text><text x="380" y="198">task to obtain the</text><text x="380" y="202">certificate.</text>
  </g>
  <rect x="10" y="253" width="7" height="7" class="fill-purple"/><text x="20" y="259" class="brand-sm">KINETRA</text>
  <line x1="50" y1="261" x2="480" y2="261" class="rule"/><text x="478" y="265" class="pg" text-anchor="end">18</text>
</svg>

<!-- 20 Team -->
<svg class="slide" viewBox="0 0 491 276">
  <text x="20" y="28" class="h2">Text Added Hare</text><rect x="20" y="36" width="14" height="2" class="fill-purple"/><rect x="36" y="36" width="4" height="2" class="fill-ink"/>
  <rect x="45" y="83" width="72" height="18" class="fill-ink"/><rect x="153" y="83" width="72" height="18" class="fill-purple"/><rect x="262" y="83" width="72" height="18" class="fill-ink"/><rect x="374" y="83" width="72" height="18" class="fill-purple"/>
  <g fill="#c9c9cc">
    <circle cx="81" cy="104" r="19" role="img" aria-label="Team member portrait"/>
    <circle cx="189" cy="104" r="19" role="img" aria-label="Team member portrait"/>
    <circle cx="298" cy="104" r="19" role="img" aria-label="Team member portrait"/>
    <circle cx="410" cy="104" r="19" role="img" aria-label="Team member portrait"/>
  </g>
  <g font-size="6.5" font-weight="700" class="fill-ink" text-anchor="middle"><text x="81" y="138">ALAN REEVE</text><text x="189" y="138">NORA VALE</text><text x="298" y="138">ALAN REEVE</text><text x="410" y="138">NORA VALE</text></g>
  <g class="fine" font-size="3.6" text-anchor="middle">
    <text x="81" y="145">ipsum dolor sit amet, cons</text><text x="81" y="149">ectetuer adipiscing elit, sed</text><text x="81" y="153">diam nonummy nibh</text><text x="81" y="163">ut laoreet dolore magna</text><text x="81" y="167">aliquam erat volutpat. Ut</text><text x="81" y="171">wisi enim ad minim veniam,</text>
    <text x="189" y="145">ipsum dolor sit amet, cons</text><text x="189" y="149">ectetuer adipiscing elit, sed</text><text x="189" y="153">diam nonummy nibh</text><text x="189" y="163">aliquam erat volutpat. Ut</text><text x="189" y="167">wisi enim ad minim veniam,</text><text x="189" y="171">quis nostrud</text>
    <text x="298" y="145">ipsum dolor sit amet, cons</text><text x="298" y="149">ectetuer adipiscing elit, sed</text><text x="298" y="153">diam nonummy nibh</text><text x="298" y="163">dolore magna aliquam erat</text><text x="298" y="167">Ut wisi enim ad minim</text><text x="298" y="171">veniam, quis nostrud</text>
    <text x="410" y="145">ipsum dolor sit amet, cons</text><text x="410" y="149">ectetuer adipiscing elit, sed</text><text x="410" y="153">diam nonummy nibh</text><text x="410" y="163">aliquam erat volutpat. Ut</text><text x="410" y="167">wisi enim ad minim veniam,</text><text x="410" y="171">quis nostrud</text>
  </g>
  <rect x="10" y="253" width="7" height="7" class="fill-purple"/><text x="20" y="259" class="brand-sm">KINETRA</text>
  <line x1="50" y1="261" x2="480" y2="261" class="rule"/><text x="478" y="265" class="pg" text-anchor="end">19</text>
</svg>

<!-- 21 Thank you -->
<svg class="slide" viewBox="0 0 491 276">
  <text x="254" y="86" font-size="22" font-weight="700" class="fill-ink">Thank You</text>
  <g class="stroke-purple" stroke-width="1.6"><path d="M258 106 q0 8 8 9 l2-3 -3-3 -2 1 q-2-1-3-3 l1-2 -3-3 z" class="fill-purple"/></g>
  <polygon points="256,133 268,138 262,140 260,146" class="fill-purple"/>
  <path d="M256 168 l6-6 6 6 v6 h-12 z" class="fill-purple"/>
  <g class="stroke-ink" stroke-width=".8"><line x1="277" y1="104" x2="277" y2="120"/><line x1="277" y1="132" x2="277" y2="148"/><line x1="277" y1="160" x2="277" y2="178"/></g>
  <g font-size="6" class="small" fill="#555"><text x="285" y="110">+44 7700 900 412</text><text x="285" y="118">+44 7700 900 413</text><text x="285" y="138">www.kinetra.io</text><text x="285" y="146">hello@kinetra.io</text><text x="285" y="166">88 Forge Lane, Halden,</text><text x="285" y="174">North Region, 40219.</text></g>
  <polygon points="215,228 238,208 491,208 491,256 215,256" class="fill-ink"/>
  <text x="250" y="242" font-size="20" font-weight="600" letter-spacing="5" class="w">KINETRA</text>
</svg>

</main>
</body>
</html>
```